Looking for a professional, clean and crisp business card

I am in the underground utilities industry and am just looking for a really impressive business card. I would like our card to be white with our symbol crisp and clear with it protruding. I also have a business partner that will require his name and info on the card once the design is set. I would like to have our website info on the card which is;
http://granitetrenchco.example/

Contact Information for Business Card

Website, contact name, number and email

```html
<!DOCTYPE html>
<html lang="en">
<head>
<meta charset="utf-8">
<title>Granite Trench Co — Business Card</title>
<link href="https://fonts.googleapis.com/css2?family=Roboto:wght@400;700&display=swap" rel="stylesheet">
<style>
  :root {
    --backdrop: #e6e6e8;
    --card-white: #ffffff;
    --card-dark: #2b2b2d;
    --accent-blue: #3556a8;
    --text-grey: #4a4a4a;
    --rule: #555555;
    --mist-top: rgba(238, 240, 248, 0);
    --mist-bottom: #e6e9f5;
    --shade-dark: #1f1f21;
    --shade-light: #5e5e62;
  }
  * { box-sizing: border-box; margin: 0; padding: 0; }
  html, body {
    width: 1200px; height: 801px; overflow: hidden;
    background: var(--backdrop);
    font-family: "Roboto", Arial, sans-serif;
  }
  .stage {
    position: relative; width: 1200px; height: 801px;
    display: flex; align-items: center; justify-content: center; gap: 50px;
  }
  .card {
    position: relative; width: 520px; height: 300px; overflow: hidden;
    border-bottom: 3px solid var(--accent-blue);
    box-shadow: 0 10px 24px rgba(0,0,0,0.18);
  }

  /* front */
  .card--front { background: var(--card-white); }
  .front-scenery {
    position: absolute; left: 0; right: 0; bottom: 0; height: 180px;
    background: linear-gradient(180deg, var(--mist-top) 0%, var(--mist-bottom) 100%);
  }
  .brand-mark {
    position: absolute; top: 34px; right: 40px;
    display: flex; align-items: center; gap: 10px;
  }
  .brand-mark__dot {
    width: 14px; height: 14px; border-radius: 50%; background: var(--accent-blue);
  }
  .brand-mark__name {
    font-weight: 700; font-size: 24px; color: #1c1c1e; letter-spacing: 0.3px;
  }
  .person { position: absolute; left: 30px; top: 140px; }
  .person__name { font-size: 22px; font-weight: 700; color: var(--accent-blue); }
  .person__role { font-size: 13px; color: var(--text-grey); margin-top: 3px; }
  .divider {
    position: absolute; left: 30px; right: 40px; top: 190px;
    height: 1px; background: var(--rule);
  }
  .contacts {
    position: absolute; left: 30px; top: 204px; list-style: none;
    font-size: 13px; color: var(--text-grey); line-height: 22px;
  }
  .contacts li { display: flex; align-items: center; gap: 10px; }
  .contacts svg {
    width: 12px; height: 12px; flex: none;
    fill: none; stroke: var(--accent-blue); stroke-width: 1.6;
  }
  .web-link { color: var(--accent-blue); }

  /* back */
  .card--back { background: var(--card-dark); }
  .back-brand {
    position: absolute; top: 60px; right: 50px;
    color: var(--card-white); font-weight: 700;
    font-size: 34px; letter-spacing: 1.5px;
  }
  .back-scenery {
    position: absolute; left: 0; right: 0; bottom: 0; height: 170px;
    background: linear-gradient(110deg, var(--shade-dark) 0%, var(--shade-dark) 40%, var(--shade-light) 100%);
    opacity: 0.85;
  }
</style>
</head>
<body>
<main class="stage">
  <article class="card card--front">
    <div class="front-scenery" role="img" aria-label="Faint snowy mountain range illustration"></div>
    <div class="brand-mark">
      <span class="brand-mark__dot"></span>
      <span class="brand-mark__name">Granite Trench Co</span>
    </div>
    <div class="person">
      <p class="person__name">Dale Merrow</p>
      <p class="person__role">Owner</p>
    </div>
    <div class="divider"></div>
    <ul class="contacts">
      <li><svg viewBox="0 0 12 12"><path d="M2 1 L4 1 L5 4 L3.5 5 Q5 8 7 8.5 L8 7 L11 8 L11 10 Q6 11 2 6 Q1 3 2 1 Z"/></svg><span>604-555-0182(DIGS)</span></li>
      <li><svg viewBox="0 0 12 12"><rect x="1" y="2.5" width="10" height="7"/><path d="M1 2.5 L6 6.5 L11 2.5"/></svg><span>Dale@granitetrenchco.example</span></li>
      <li><svg viewBox="0 0 12 12"><circle cx="6" cy="6" r="5"/><path d="M1 6 H11 M6 1 Q3 6 6 11 Q9 6 6 1"/></svg><span>www.<span class="web-link">granitetrenchco</span>.example</span></li>
    </ul>
  </article>

  <article class="card card--back">
    <p class="back-brand">Granite Trench Co</p>
    <div class="back-scenery" role="img" aria-label="Dark mountain peaks illustration"></div>
  </article>
</main>
</body>
</html>
```